Photoshop Design Project

Tourist information board for an app. Words "Tourist information" (editable) is written or engraved in black on a piece of wood nailed to the wooden framed board. Image is normally found on nature walks or at resorts.
Wooden background,wooden frames, wooden posts. 1024x768. Little emphasis on the posts. Just as long its visible but maximise the posting area.
Posting area to be divided into 8 sections with separate wooden framed window like panes.
The middle section is to accomodate a small map, so it has to be slightly larger than the other 7 sections.
Please include paper into the separate sections and leave it blank for me to insert pictures and text. It'll be great if you could specify the area and I will just edit.
As natural as can be but a little cartoon texture to it just for enhancement since its for a game app.

```html
<!DOCTYPE html>
<html lang="en">
<head>
<meta charset="utf-8">
<title>Tourist information board</title>
<link rel="stylesheet" href="https://fonts.googleapis.com/css2?family=Almendra+SC&display=swap">
<style>
  :root {
    --page: #ffffff;
    --plank-light: #b9733c;
    --plank-mid: #9a5a2a;
    --plank-dark: #6e3b17;
    --plank-line: #5a2e10;
    --log-light: #a57045;
    --log-mid: #7f5030;
    --log-dark: #4f2f18;
    --log-tip: #e9c98c;
    --rope: #c9a66b;
    --pane-frame: #4a2610;
    --title-ink: #2a160a;
    --title-edge: #e8c48a;
  }
  * { box-sizing: border-box; margin: 0; padding: 0; }
  html, body { width: 1200px; height: 900px; overflow: hidden; background: var(--page); }
  .canvas { position: relative; width: 1200px; height: 900px; }

  .board {
    position: absolute; left: 155px; top: 150px; width: 894px; height: 590px;
    background:
      repeating-linear-gradient(90deg, transparent 0 44px, var(--plank-line) 44px 46px),
      linear-gradient(90deg, var(--plank-mid), var(--plank-light) 30%, var(--plank-mid) 55%, var(--plank-light) 80%, var(--plank-mid));
  }

  .frame { position: absolute; inset: 0; width: 1200px; height: 900px; }

  .board-title {
    position: absolute; left: 155px; width: 894px; top: 168px;
    text-align: center;
    font-family: "Almendra SC", serif; font-size: 50px; line-height: 1;
    color: var(--title-ink); letter-spacing: 2px;
    -webkit-text-stroke: 1px var(--title-edge);
  }

  .pane {
    position: absolute;
    border: 6px solid var(--pane-frame);
    box-shadow: 0 2px 4px rgba(0,0,0,.45);
  }
  .pane--autumn-sun { left: 170px; top: 255px; width: 255px; height: 149px; background: linear-gradient(160deg, #e8601c, #f6b040 45%, #8a4a1c); }
  .pane--overwater-hut { left: 170px; top: 416px; width: 255px; height: 146px; background: linear-gradient(180deg, #4d8fd0, #9fd2ea 45%, #e9dcc4 75%, #2e4a1f); }
  .pane--tulips { left: 170px; top: 574px; width: 255px; height: 150px; background: linear-gradient(180deg, #2a79d8, #8cc4f0 55%, #4fa62a 78%, #2c7a16); }
  .pane--town-map { left: 437px; top: 255px; width: 331px; height: 307px; background: linear-gradient(135deg, #3d9a3a, #6cc24a 50%, #3d9a3a); }
  .pane--beach-hammock { left: 475px; top: 574px; width: 257px; height: 150px; background: linear-gradient(180deg, #7cb6e4, #3aa3c8 45%, #e8e0cc 70%, #d9cbaa); }
  .pane--autumn-avenue { left: 777px; top: 255px; width: 261px; height: 149px; background: linear-gradient(180deg, #b88a3a, #6a4a1e 55%, #c98c2a); }
  .pane--pool-terrace { left: 777px; top: 416px; width: 261px; height: 146px; background: linear-gradient(180deg, #2a72d0, #a8d4f2 40%, #2fb6d8 65%, #b0522c); }
  .pane--green-leaves { left: 777px; top: 574px; width: 261px; height: 150px; background: radial-gradient(circle at 50% 40%, #b6e05a, #6aa81e 55%, #3c6e10); }

  .bird { position: absolute; border-radius: 50%; }
  .bird--orange { left: 195px; top: 44px; width: 90px; height: 60px; background: radial-gradient(circle at 55% 45%, #ffc34d, #f2922a); }
  .bird--blue { left: 938px; top: 44px; width: 98px; height: 60px; background: radial-gradient(circle at 45% 45%, #5fd6f0, #1d9fd0); }

  .grass { position: absolute; border-radius: 50% 50% 0 0; background: linear-gradient(180deg, #7cc63a, #2f7a16); }
  .grass--left { left: 55px; top: 812px; width: 160px; height: 88px; }
  .grass--right { left: 980px; top: 818px; width: 185px; height: 82px; }
</style>
</head>
<body>
<main class="canvas">
  <div class="board"></div>

  <svg class="frame" viewBox="0 0 1200 900" aria-hidden="true">
    <defs>
      <linearGradient id="post-grain" x1="0" x2="1" y1="0" y2="0">
        <stop offset="0" stop-color="var(--log-dark)"/>
        <stop offset=".4" stop-color="var(--log-light)"/>
        <stop offset="1" stop-color="var(--log-dark)"/>
      </linearGradient>
      <linearGradient id="log-grain" x1="0" x2="0" y1="0" y2="1">
        <stop offset="0" stop-color="var(--log-light)"/>
        <stop offset=".5" stop-color="var(--log-mid)"/>
        <stop offset="1" stop-color="var(--log-dark)"/>
      </linearGradient>
    </defs>

    <!-- posts -->
    <g class="posts">
      <polygon points="100,60 129,6 158,60 158,890 100,890" fill="url(#post-grain)"/>
      <polygon points="100,60 129,6 158,60" fill="var(--log-tip)"/>
      <polygon points="1049,60 1078,6 1107,60 1107,890 1049,890" fill="url(#post-grain)"/>
      <polygon points="1049,60 1078,6 1107,60" fill="var(--log-tip)"/>
    </g>

    <!-- rails -->
    <g class="rails">
      <polygon points="12,128 70,103 1130,103 1189,128 1130,152 70,152" fill="url(#log-grain)"/>
      <polygon points="12,128 70,103 70,152" fill="var(--log-tip)"/>
      <polygon points="1189,128 1130,103 1130,152" fill="var(--log-tip)"/>
      <polygon points="12,758 70,733 1130,733 1189,758 1130,783 70,783" fill="url(#log-grain)"/>
      <polygon points="12,758 70,733 70,783" fill="var(--log-tip)"/>
      <polygon points="1189,758 1130,733 1130,783" fill="var(--log-tip)"/>
    </g>

    <!-- rope bindings on rails -->
    <g class="rope-bindings" fill="var(--rope)" stroke="#7a5a2c" stroke-width="1">
      <rect x="225" y="101" width="8" height="53" rx="3"/>
      <rect x="400" y="101" width="8" height="53" rx="3"/>
      <rect x="570" y="101" width="8" height="53" rx="3"/>
      <rect x="760" y="101" width="8" height="53" rx="3"/>
      <rect x="930" y="101" width="8" height="53" rx="3"/>
      <rect x="225" y="731" width="8" height="54" rx="3"/>
      <rect x="420" y="731" width="8" height="54" rx="3"/>
      <rect x="620" y="731" width="8" height="54" rx="3"/>
      <rect x="800" y="731" width="8" height="54" rx="3"/>
      <rect x="960" y="731" width="8" height="54" rx="3"/>
    </g>

    <!-- rope bindings on posts -->
    <g class="rope-bindings" fill="var(--rope)" stroke="#7a5a2c" stroke-width="1">
      <rect x="98" y="230" width="62" height="7" rx="3"/>
      <rect x="98" y="400" width="62" height="7" rx="3"/>
      <rect x="98" y="570" width="62" height="7" rx="3"/>
      <rect x="1047" y="230" width="62" height="7" rx="3"/>
      <rect x="1047" y="400" width="62" height="7" rx="3"/>
      <rect x="1047" y="570" width="62" height="7" rx="3"/>
    </g>

    <!-- corner lashings -->
    <g class="lashings" stroke="var(--rope)" stroke-width="9" stroke-linecap="round">
      <line x1="100" y1="150" x2="158" y2="104"/>
      <line x1="1049" y1="104" x2="1107" y2="150"/>
      <line x1="100" y1="734" x2="158" y2="782"/>
      <line x1="1049" y1="782" x2="1107" y2="734"/>
    </g>
  </svg>

  <h1 class="board-title">Tourist information</h1>

  <div class="pane pane--autumn-sun" role="img" aria-label="Photo: red autumn leaves with sunlight"></div>
  <div class="pane pane--town-map" role="img" aria-label="Illustrated green town map with river and buildings"></div>
  <div class="pane pane--autumn-avenue" role="img" aria-label="Photo: avenue of golden autumn trees"></div>
  <div class="pane pane--overwater-hut" role="img" aria-label="Photo: thatched hut at the end of a beach jetty"></div>
  <div class="pane pane--pool-terrace" role="img" aria-label="Photo: resort pool terrace with palm and parasol by the sea"></div>
  <div class="pane pane--tulips" role="img" aria-label="Photo: tulips on green grass under blue sky"></div>
  <div class="pane pane--beach-hammock" role="img" aria-label="Photo: palm-lined beach with hammock and huts"></div>
  <div class="pane pane--green-leaves" role="img" aria-label="Photo: close-up of fresh green leaves"></div>

  <div class="bird bird--orange" role="img" aria-label="Cartoon orange bird perched on the rail"></div>
  <div class="bird bird--blue" role="img" aria-label="Cartoon blue bird perched on the rail"></div>

  <div class="grass grass--left" role="img" aria-label="Grass tuft with a small yellow flower"></div>
  <div class="grass grass--right" role="img" aria-label="Grass tuft"></div>
</main>
</body>
</html>
```